Awesome design needed for standup comedy portal

We need a website designed for a new portal (grinvault.net) dedicated to standup comedy.

- homepage
- featured "hero" content at top
- banner advertising
- browse comics
- browse venues
- search
- signup / login
- social media links

- comic page
- name
- pictures
- calendar of performances
- list of albums (with buy buttons)
- list of specials (Streamora, Tunebox, etc. with buy buttons)
- reviews
- latest tweets
- latests picshelf photos
- links to social media accounts
- links to flmx, podcast

- venue page
- name
- pictures
- address, phone number
- calendar of events
- reviews
- latest tweets
- links to flmx, podcast

Target Market(s)

Fans of standup comedy and comedians

Number of Pages Required

3 page

Font styles to use
Sans Serif

Requirements
Must have
• Will eventually be implemented in bootstrap, so please keep that in mind

```html
<!DOCTYPE html>
<html lang="en">
<head>
<meta charset="utf-8">
<title>GrinVault — Stand Up Comedy</title>
<link href="https://fonts.googleapis.com/css2?family=Raleway:wght@400;500;700&family=Cinzel:wght@400&display=swap" rel="stylesheet">
<style>
  :root {
    --maroon: #720f10;
    --maroon-deep: #560b0c;
    --nav-text: #5a1a1c;
    --white: #ffffff;
    --brand-blue: #3b9bd8;
    --hero-title: #7a7a7a;
    --curtain: #7a0f12;
    --shadow: #050203;
  }
  * { margin: 0; padding: 0; box-sizing: border-box; }
  html, body { width: 1200px; height: 516px; overflow: hidden; background: var(--white); }
  body { font-family: "Raleway", Arial, sans-serif; position: relative; }

  .topbar {
    position: absolute; left: 0; top: 0; width: 1200px; height: 40px;
    background: var(--maroon);
  }
  .social { position: absolute; left: 93px; top: 6px; display: flex; gap: 2px; list-style: none; }
  .social a {
    display: flex; align-items: center; justify-content: center;
    width: 27px; height: 27px; border-radius: 50%;
    background: var(--maroon-deep);
    color: var(--white); font-size: 11px; font-weight: 700; text-decoration: none;
  }
  .account { position: absolute; right: 98px; top: 13px; display: flex; gap: 28px; }
  .account a { color: var(--white); font-size: 11.5px; text-decoration: none; }

  .navbar {
    position: absolute; left: 0; top: 40px; width: 1200px; height: 74px;
    background: var(--white);
  }
  .brand {
    position: absolute; left: 93px; top: 30px; display: flex; align-items: center; gap: 8px;
    text-decoration: none;
  }
  .brand-mark { width: 22px; height: 22px; background: var(--brand-blue); }
  .brand-name { font-size: 18px; font-weight: 700; color: var(--maroon); }
  .menu { position: absolute; left: 790px; top: 25px; display: flex; list-style: none; }
  .menu li { margin-right: 37px; }
  .menu a { color: var(--nav-text); font-size: 15.5px; text-decoration: none; }
  .menu .has-sub a::after {
    content: ""; display: inline-block; width: 4px; height: 4px; margin-left: 5px;
    border-right: 1px solid #b7b7b7; border-bottom: 1px solid #b7b7b7;
    transform: rotate(45deg) translateY(-4px);
  }

  .hero {
    position: absolute; left: 0; top: 114px; width: 1200px; height: 402px; overflow: hidden;
    background:
      radial-gradient(ellipse 420px 360px at 300px 200px, rgba(140,18,22,0.75), rgba(90,10,14,0.55) 55%, transparent 100%),
      linear-gradient(90deg, #2a0608 0%, var(--curtain) 20%, #5a0a0e 40%, #2a0508 62%, var(--shadow) 80%, #0b0407 100%);
  }
  .hero-title {
    position: absolute; left: 462px; top: 113px;
    font-family: "Cinzel", Georgia, serif; font-weight: 400;
    color: var(--hero-title); font-size: 120px; line-height: 146px;
    white-space: nowrap; opacity: 0.9;
  }
  .hero-title span { display: block; }
  .hero-title .line-two { padding-left: 42px; }
</style>
</head>
<body>
  <header class="topbar">
    <ul class="social">
      <li><a href="#" aria-label="Chirpline">C</a></li>
      <li><a href="#" aria-label="Voxcall">V</a></li>
      <li><a href="#" aria-label="Orbnet">O</a></li>
      <li><a href="#" aria-label="Reelcast">R</a></li>
      <li><a href="#" aria-label="Meetly">M</a></li>
    </ul>
    <nav class="account">
      <a href="#">Log in</a>
      <a href="#">Sign Up</a>
    </nav>
  </header>

  <nav class="navbar">
    <a class="brand" href="#">
      <span class="brand-mark"></span>
      <span class="brand-name">GrinVault</span>
    </a>
    <ul class="menu">
      <li><a href="#">Home</a></li>
      <li><a href="#">About Us</a></li>
      <li class="has-sub"><a href="#">Comic</a></li>
      <li><a href="#">Venue</a></li>
    </ul>
  </nav>

  <section class="hero" role="img" aria-label="Comedian performing in front of a red stage curtain with a microphone in the foreground and an audience below">
    <h1 class="hero-title"><span>Stand Up</span><span class="line-two">Comedy</span></h1>
  </section>
</body>
</html>
```